Business Card Design for Harwick Crest Management

Design a catchy business card for UK-based technology company. Creative, serious and minimalistic style.

```html
<!DOCTYPE html>
<html lang="en">
<head>
<meta charset="utf-8">
<title>Harwick Crest Management – Business Card</title>
<link href="https://fonts.googleapis.com/css2?family=Dosis:wght@300;400;500&display=swap" rel="stylesheet">
<style>
  :root {
    --card-red: #c80000;
    --block-red: #9e0000;
    --ink: #ffffff;
    --ink-soft: #f3c9c9;
    --backdrop-top: #f4f4f4;
    --backdrop-bottom: #d9d9d9;
  }
  * { box-sizing: border-box; margin: 0; padding: 0; }
  html, body { width: 1200px; height: 800px; overflow: hidden; }
  body {
    background: linear-gradient(160deg, var(--backdrop-top), var(--backdrop-bottom));
    font-family: "Dosis", sans-serif;
    color: var(--ink);
    display: flex;
    flex-direction: column;
    align-items: center;
    justify-content: center;
    gap: 34px;
  }
  .card {
    position: relative;
    width: 600px;
    height: 343px;
    background: var(--card-red);
    box-shadow: 0 6px 18px rgba(0,0,0,0.18);
  }

  /* Front */
  .brand {
    position: absolute;
    top: 30px;
    right: 36px;
    display: flex;
    align-items: center;
    gap: 10px;
    font-size: 14px;
    font-weight: 400;
    letter-spacing: 0.06em;
    text-transform: uppercase;
  }
  .brand-square {
    width: 22px;
    height: 22px;
    background: var(--block-red);
  }
  .identity {
    position: absolute;
    left: 40px;
    right: 40px;
    bottom: 98px;
    display: flex;
    align-items: baseline;
    gap: 18px;
  }
  .person-name { font-size: 32px; font-weight: 500; letter-spacing: 0.02em; }
  .person-role { font-size: 19px; font-weight: 300; letter-spacing: 0.06em; color: var(--ink-soft); }
  .rule {
    position: absolute;
    left: 40px;
    right: 40px;
    bottom: 86px;
    height: 1px;
    background: var(--ink-soft);
  }
  .contacts {
    position: absolute;
    left: 40px;
    right: 40px;
    top: 268px;
    display: flex;
    font-size: 12.5px;
    font-weight: 400;
    letter-spacing: 0.05em;
    color: var(--ink-soft);
    list-style: none;
  }
  .contacts li { padding: 0 12px; border-left: 1px solid var(--ink-soft); line-height: 18px; }
  .contacts li:first-child { padding-left: 0; border-left: 0; }

  /* Back */
  .back-square {
    position: absolute;
    left: 40px;
    top: 96px;
    width: 110px;
    height: 110px;
    background: var(--block-red);
  }
  .back-name {
    position: absolute;
    left: 172px;
    top: 100px;
    font-size: 28px;
    font-weight: 500;
    line-height: 1.15;
    letter-spacing: 0.02em;
  }
  .promise {
    position: absolute;
    left: 172px;
    top: 178px;
    font-size: 20px;
    font-weight: 300;
    letter-spacing: 0.06em;
  }
  .signature {
    position: absolute;
    right: 40px;
    bottom: 32px;
    font-size: 11px;
    letter-spacing: 0.05em;
    color: var(--ink-soft);
  }
</style>
</head>
<body>
  <section class="card card-front">
    <div class="brand"><span class="brand-square"></span>Harwick Crest Management</div>
    <div class="identity">
      <span class="person-name">Alan Marsh</span>
      <span class="person-role">creative director</span>
    </div>
    <div class="rule"></div>
    <ul class="contacts">
      <li>alanmarsh@harwickcrest.com</li>
      <li>+44 20 7946 0321</li>
      <li>Ashby Court, 3rd Floor, London</li>
    </ul>
  </section>

  <section class="card card-back">
    <div class="back-square"></div>
    <p class="back-name">Harwick Crest<br>Management</p>
    <p class="promise">Built with care, made to last.</p>
    <p class="signature">Harwick Crest Management</p>
  </section>
</body>
</html>
```